Typing Service Business Card Design

Need a new business card design for new logo update. The Keyline Crew is an outsourced typing service. We type audio / voice files into word documents. We are a professional service that is recognised in the industry over the past 15 years and have a strong connection to our brand. The final design should be professional, simple, yet effective.

Business

Contact Information for Business Card

Rosalind Varga
Director

rosalind@kbq.com.au
www.thekeylinecrewbase.com.au

```html
<!DOCTYPE html>
<html lang="en">
<head>
<meta charset="utf-8">
<title>The Keyline Crew – Business Card</title>
<link rel="stylesheet" href="https://fonts.googleapis.com/css2?family=Arimo:wght@400;700&family=Mulish:wght@400&display=swap">
<style>
  :root {
    --bg: #e9e6e1;
    --pink: #c93a90;
    --pink-light: #dc5fae;
    --black: #1f1f1f;
    --black-soft: #2c2c2c;
    --white: #ffffff;
    --grey: #5a5a5a;
    --ink: #2a2a2a;
  }
  * { box-sizing: border-box; margin: 0; padding: 0; }
  html, body { width: 1200px; height: 843px; overflow: hidden; }
  body {
    background: var(--bg);
    display: flex;
    align-items: center;
    justify-content: center;
    gap: 40px;
    font-family: "Mulish", sans-serif;
  }
  .card {
    position: relative;
    width: 520px;
    height: 317px;
    border-radius: 6px;
    overflow: hidden;
    box-shadow: 0 10px 28px rgba(0,0,0,0.18);
  }

  /* Back side */
  .card--back {
    background: linear-gradient(160deg, var(--black-soft), var(--black));
    display: flex;
    flex-direction: column;
    align-items: center;
    justify-content: center;
    gap: 8px;
  }
  .brand-name {
    font-family: "Arimo", sans-serif;
    font-weight: 700;
    color: var(--pink);
    letter-spacing: 0.2px;
    white-space: nowrap;
  }
  .card--back .brand-name { font-size: 30px; }
  .tagline {
    font-family: "Arimo", sans-serif;
    font-weight: 400;
    white-space: nowrap;
  }
  .card--back .tagline { font-size: 16px; color: #d8d8d8; margin-left: 90px; }

  /* Front side */
  .card--front { background: var(--white); }
  .front-band { position: absolute; top: 0; left: 0; }
  .holder {
    position: absolute;
    right: 30px;
    top: 56px;
    text-align: right;
    color: var(--white);
    font-family: "Arimo", sans-serif;
  }
  .holder-name { font-size: 25px; font-weight: 700; letter-spacing: 0.3px; }
  .holder-role { font-size: 16px; margin-top: 4px; }
  .contacts {
    position: absolute;
    left: 28px;
    top: 196px;
    list-style: none;
    color: var(--grey);
    font-size: 16px;
  }
  .contacts li {
    display: flex;
    align-items: center;
    gap: 9px;
    height: 26px;
    white-space: nowrap;
  }
  .contacts svg { flex: none; }
  .front-brand {
    position: absolute;
    right: 30px;
    bottom: 34px;
    display: flex;
    flex-direction: column;
    align-items: flex-end;
    gap: 6px;
  }
  .front-brand .brand-name { font-size: 24px; }
  .front-brand .tagline { font-size: 15px; color: var(--ink); }
</style>
</head>
<body>
  <section class="card card--back" aria-label="Business card back">
    <div class="brand-name">The Keyline Crew</div>
    <div class="tagline">You speak. We key.</div>
  </section>

  <section class="card card--front" aria-label="Business card front">
    <svg class="front-band" width="520" height="317" viewBox="0 0 520 317" aria-hidden="true">
      <defs>
        <linearGradient id="bandFill" x1="0" y1="0" x2="1" y2="1">
          <stop offset="0" stop-color="#e06cb3"/>
          <stop offset="1" stop-color="#c4348b"/>
        </linearGradient>
      </defs>
      <path d="M0,0 H520 V118 Q520,140 498,140 H150 L28,160 L48,118 H0 Z" fill="url(#bandFill)"/>
    </svg>

    <div class="holder">
      <div class="holder-name">Rosalind Varga</div>
      <div class="holder-role">Director</div>
    </div>

    <ul class="contacts">
      <li>
        <svg width="14" height="11" viewBox="0 0 14 11" aria-hidden="true">
          <rect width="14" height="11" rx="1.5" fill="var(--pink)"/>
          <path d="M1.5,2 L7,6 L12.5,2" stroke="#fff" stroke-width="1.3" fill="none"/>
        </svg>
        <span>rosalind@kbq.com.au</span>
      </li>
      <li>
        <svg width="14" height="14" viewBox="0 0 14 14" aria-hidden="true">
          <circle cx="7" cy="7" r="7" fill="var(--pink)"/>
          <circle cx="7" cy="7" r="4.2" stroke="#fff" stroke-width="1" fill="none"/>
          <path d="M2.8,7 H11.2 M7,2.8 V11.2" stroke="#fff" stroke-width="1"/>
        </svg>
        <span>thekeylinecrewbase.com.au</span>
      </li>
    </ul>

    <div class="front-brand">
      <div class="brand-name">The Keyline Crew</div>
      <div class="tagline">You speak. We key.</div>
    </div>
  </section>
</body>
</html>
```